Cosmetic injections clinic needs a fresh looking business card

We need a business card using the supplied logo and color scheme to attract future clients to our clinic. It should be modern and fresh, eye catching and not too busy. Simple and to the point is best. I would like two sided designs with the front indicating address and contact information, and the back in full color with white logo and descriptive information also provided.
Target Market(s)
Clients looking for non surgical beauty enhancements.
Contact Information for Business Card
Lumivela
14, 415 Carrow Ridge Road
Brennmoor, Westhaven
K2P 7W3
Phone: 431-662-0974
Email: info@lumivela-example.com
Requirements
Must have
- -Logo supplied with the name and address of the clinic
- -Back of card in full color with white logo with A small line of text indicating both of the following: Anti aging consultants and cosmetic injectables
- Located inside the Wayfarer Care Group

```html
<!DOCTYPE html>
<html lang="en">
<head>
<meta charset="utf-8">
<title>Lumivela — Business Card</title>
<link href="https://fonts.googleapis.com/css2?family=Work+Sans:wght@400;500;600&display=swap" rel="stylesheet">
<style>
  :root {
    --bg: #3a3a3d;
    --card-white: #ffffff;
    --purple: #7a4fa3;
    --purple-dark: #5c3a86;
    --teal: #1fb39a;
    --pink: #e0409a;
    --pink-deep: #c42d82;
    --ink: #3b3b3b;
    --white: #ffffff;
  }
  * { margin: 0; padding: 0; box-sizing: border-box; }
  html, body { width: 1200px; height: 900px; overflow: hidden; }
  body {
    background: var(--bg);
    font-family: "Work Sans", sans-serif;
    display: flex;
    flex-direction: column;
    align-items: center;
    justify-content: center;
    gap: 50px;
  }
  .card {
    position: relative;
    width: 630px;
    height: 360px;
    border-radius: 18px;
    overflow: hidden;
  }
  .card-front { background: var(--card-white); }
  .card-front .wave { position: absolute; inset: 0; }
  .brand-mark {
    position: absolute;
    left: 50px;
    top: 100px;
    display: flex;
    align-items: center;
    gap: 12px;
  }
  .brand-dot {
    width: 26px; height: 26px;
    border-radius: 50%;
    background: var(--pink);
  }
  .brand-name {
    font-size: 44px;
    font-weight: 600;
    color: var(--purple-dark);
    letter-spacing: 0.5px;
  }
  .divider {
    position: absolute;
    left: 300px;
    top: 62px;
    width: 2px;
    height: 170px;
    background: var(--pink);
  }
  .contact {
    position: absolute;
    left: 324px;
    top: 60px;
    color: var(--ink);
  }
  .person-name {
    font-size: 24px;
    font-weight: 500;
    color: var(--purple);
    letter-spacing: 1.5px;
    text-transform: uppercase;
  }
  .person-role { font-size: 15px; margin-top: 2px; }
  .address { font-size: 15px; line-height: 1.3; margin-top: 10px; }
  .lines { list-style: none; margin-top: 10px; font-size: 15px; line-height: 1.45; }
  .lines li { display: flex; align-items: center; gap: 8px; }
  .lines svg { width: 11px; height: 11px; fill: var(--purple); flex: none; }
  .card-back {
    background: linear-gradient(135deg, var(--pink) 0%, var(--pink-deep) 100%);
    display: flex;
    flex-direction: column;
    align-items: center;
    justify-content: center;
    gap: 22px;
  }
  .back-mark { display: flex; align-items: center; gap: 14px; }
  .back-mark .brand-dot { background: var(--white); width: 30px; height: 30px; }
  .back-mark .brand-name { color: var(--white); font-size: 58px; }
  .tagline { color: var(--white); font-size: 17px; letter-spacing: 0.5px; }
</style>
</head>
<body>
  <section class="card card-front">
    <svg class="wave" viewBox="0 0 630 360" preserveAspectRatio="none">
      <path d="M0,212 C150,228 250,280 350,318 C440,348 540,354 630,356 L630,360 L0,360 Z" fill="var(--purple)"/>
      <path d="M0,196 C150,212 250,264 350,302 C440,332 540,340 630,344" fill="none" stroke="var(--teal)" stroke-width="5"/>
    </svg>
    <div class="brand-mark">
      <span class="brand-dot"></span>
      <span class="brand-name">Lumivela</span>
    </div>
    <div class="divider"></div>
    <div class="contact">
      <h1 class="person-name">Daria Whitlock</h1>
      <p class="person-role">Founder</p>
      <p class="address">14, 415 Carrow Ridge Road<br>Brennmoor, Westhaven<br>K2P 7W3</p>
      <ul class="lines">
        <li><svg viewBox="0 0 24 24"><path d="M6.6 10.8a15 15 0 0 0 6.6 6.6l2.2-2.2c.3-.3.7-.4 1-.2 1.1.4 2.3.6 3.6.6.6 0 1 .4 1 1V20c0 .6-.4 1-1 1A17 17 0 0 1 3 4c0-.6.4-1 1-1h3.5c.6 0 1 .4 1 1 0 1.3.2 2.5.6 3.6.1.3 0 .7-.2 1z"/></svg>431-662-0974</li>
        <li><svg viewBox="0 0 24 24"><path d="M2 5h20v14H2z M4 7v.5l8 5 8-5V7z" fill-rule="evenodd"/></svg>info@lumivela-example.com</li>
        <li><svg viewBox="0 0 24 24"><circle cx="12" cy="12" r="10"/></svg>www.lumivela-example.com</li>
      </ul>
    </div>
  </section>

  <section class="card card-back">
    <div class="back-mark">
      <span class="brand-dot"></span>
      <span class="brand-name">Lumivela</span>
    </div>
    <p class="tagline">Anti aging consultants and cosmetic injectables</p>
  </section>
</body>
</html>
```